Honey Label Design (145 × 55 mm) – Premium / Minimal Style

Project Description
I am looking for a professional label design for a 500 g honey jar (twist-off, copper-colored lid).
The design should look premium, elegant, and minimal, reflecting natural quality and regional authenticity.
I expect two design proposals from each designer:

One concept based strictly on my color and style guidelines
One completely free creative concept (designer's own interpretation)

⚠️ Important: The layout and positioning of all elements must follow my specifications exactly (see below). Creativity is welcome in style, colors, and typography—but not in layout structure and content.

Label Size and Constraints

Final size: 145 mm × 55 mm (landscape)
All elements must remain fully within the label area
No part (especially the hexagon) may extend beyond the label boundaries

Design Style

Minimal, clean, premium
No clutter, no excessive colors
Preferred colors:

Warm natural tones (honey, beige, brown)
Inspired by the branding of: www.wabenhof-laden. de
Subtle copper tone accents (to match the lid)

Background

Very subtle illustrated/sketched background
Motif:

Wildflower meadow (foreground)
Mixed forest (background)

Style should be fine line / sketch style, not photorealistic
The background must remain very soft so text remains clearly readable

Central Element (Mandatory)

A hexagon (honeycomb shape) centered on the label
Inside text:

“GERMAN HONEY”
“500 g”

The hexagon must be:

Fully inside the label (no overlapping, my example is wrong)
Visually balanced and centered

Left Text Block (Important)
The following content (in german) must be placed left-aligned (not centered!):
Bottling point:
Henrik Dollmann Beekeeping
Lindenkamper Weg 17
07318 Saalfeld
Tel.: 03671 5274061
mail@wabenhof-laden.example
Typography must be clean and clearly structured.

Mandatory White Fields (Very Important)
There must be exactly 3 white boxes:
Size:

Each: 28 mm × 12 mm
No visible border

Positioning (must follow exactly):

Bottom center

Completely blank (for honey type)

Right side – upper field

Text above: “Best before:”

Right side – lower field (directly below)

Text above: “Lot number”

⚠️ All three fields must:

Be identical in size
Be perfectly aligned
Match the layout shown in the reference image

Layout Rules (Strict)

The arrangement of elements is fixed and must not be changed
Center field must be directly below the hexagon
Right-side fields must be vertically aligned
Left text must remain left-aligned

goal
The label should communicate:

High quality / premium honey
Regional trust and authenticity
Clean and professional print-ready design

Reference
A reference image is provided showing:

exact placement of all fields
general layout structure

⚠️ The reference is for layout guidance only — not for copying design style.
Updates

All mandatory information must be in German like the address
Bottling point:
Henrik Dollmann Beekeeping
Lindenkamper W. 17
07318 Saalfeld
Tel.: 03671 5274061
www.wabenhof-laden.example

Target Market(s)

Germany

Font styles to use
Sans Serif
Other font styles liked:
• Montserrat, Open Sans, Libre Baskerville

Colors
00AB8E
00BBA5
67D7C9
C6EFE9
E9F9F6
59FF00
82FF00
B8FF75
E3FFCB
F4FFEA
FFF300
FFF600
FEFA6F
FFFEC7
FFFEE8
FFC000
F8CF3A
FAE287
FDF2CF
FEFAEE
F0912C
F2A743
F7CA91
FBE8D2
FDF5EE
EE7325
F08F49
F5BC92
FAE3D3
FDF4ED

Requirements
Must have
• Mandatory Information on Honey Labels (Germany / EU) (Product Name, Country of origin, Net quantity, Minimum durability date (placeholder), Name and address of the food business operator, Batch / lot identification (placeholder), Special warning for infants “Not suitable for infants under 12 months”

```html
<!DOCTYPE html>
<html lang="de">
<head>
<meta charset="utf-8">
<title>Honig-Etikett 500 g</title>
<link href="https://fonts.googleapis.com/css2?family=Open+Sans:wght@600;700&family=Playfair+Display:wght@400;700&display=swap" rel="stylesheet">
<style>
  :root {
    --stage: #b9b9b9;
    --frame: #4a4a4a;
    --paper: #f6eddb;
    --ink: #3b3835;
    --gold-light: #f6d36b;
    --gold: #d9a521;
    --gold-dark: #b8820f;
    --copper: #ee7325;
    --field: #ffffff;
  }
  * { box-sizing: border-box; margin: 0; padding: 0; }
  html, body { width: 1200px; height: 455px; overflow: hidden; background: var(--stage); }
  .canvas { position: relative; width: 1200px; height: 455px; }

  .label {
    position: absolute; left: 106px; top: 40px; width: 987px; height: 376px;
    background: var(--paper); border: 4px solid var(--frame); overflow: hidden;
    box-shadow: 0 2px 6px rgba(0,0,0,.25);
  }
  .label > * { position: absolute; }

  .art { pointer-events: none; }
  .art--forest {
    left: 0; top: 0; width: 979px; height: 190px;
    background: linear-gradient(180deg, rgba(228,212,176,.55) 0%, rgba(228,212,176,.25) 60%, rgba(228,212,176,0) 100%);
  }
  .art--flowers-left {
    left: 0; top: 238px; width: 80px; height: 130px;
    background: radial-gradient(ellipse at 35% 55%, rgba(214,140,180,.55) 0%, rgba(120,150,100,.35) 55%, rgba(246,237,219,0) 80%);
  }
  .art--flowers-right {
    left: 880px; top: 245px; width: 99px; height: 123px;
    background: radial-gradient(ellipse at 55% 55%, rgba(220,90,70,.45) 0%, rgba(150,170,100,.35) 50%, rgba(246,237,219,0) 80%);
  }

  .sans { font-family: "Open Sans", Arial, sans-serif; font-weight: 700; color: var(--ink); line-height: 1; white-space: nowrap; }
  .serif { font-family: "Playfair Display", Georgia, serif; color: var(--ink); line-height: 1; white-space: nowrap; }

  .operator__heading { left: 139px; top: 80px; font-size: 16px; letter-spacing: .3px; }
  .operator__address { left: 72px; top: 128px; font-size: 22px; font-weight: 700; line-height: 30px; }
  .operator__phone { left: 72px; top: 254px; font-size: 16px; letter-spacing: 1.6px; font-weight: 600; }
  .operator__web { left: 72px; top: 281px; font-size: 16px; }
  .shop-name { left: 178px; top: 323px; display: flex; align-items: center; gap: 6px; font-size: 12px; color: var(--copper); }
  .shop-name__dot { width: 12px; height: 12px; border-radius: 50%; background: var(--copper); }

  .honey__country { left: 488px; top: 92px; width: 0; display: flex; justify-content: center; font-size: 15px; font-weight: 700; letter-spacing: 2.5px; }
  .honey__name { left: 488px; top: 107px; width: 0; display: flex; justify-content: center; font-size: 44px; font-weight: 700; letter-spacing: 3px; }
  .honey__weight { left: 488px; top: 172px; width: 0; display: flex; justify-content: center; font-size: 26px; }

  .field-label { width: 190px; text-align: center; font-size: 15px; font-weight: 600; }
  .field-label--best { left: 672px; top: 9px; letter-spacing: .4px; }
  .field-label--lot { left: 672px; top: 127px; letter-spacing: 2px; }
  .field { width: 190px; height: 81px; background: var(--field); }
  .field--best { left: 672px; top: 40px; }
  .field--lot { left: 672px; top: 159px; }
  .field--type { left: 393px; top: 275px; }

  .infant-warning { left: 672px; top: 262px; width: 190px; text-align: center; font-size: 12px; font-weight: 600; line-height: 16px; white-space: normal; }

  .lines { left: 0; top: 0; width: 979px; height: 368px; }
</style>
</head>
<body>
<div class="canvas">
  <div class="label">
    <div class="art art--forest" role="img" aria-label="Feine Skizze eines Mischwaldes und einer Wiese im Hintergrund"></div>
    <div class="art art--flowers-left" role="img" aria-label="Illustration von Wildblumen unten links"></div>
    <div class="art art--flowers-right" role="img" aria-label="Illustration einer Wildblumenwiese mit Mohn unten rechts"></div>

    <svg class="lines" viewBox="0 0 979 368" aria-hidden="true">
      <defs>
        <linearGradient id="gold" x1="0" y1="0" x2="1" y2="1">
          <stop offset="0" stop-color="var(--gold-light)"/>
          <stop offset=".5" stop-color="var(--gold)"/>
          <stop offset="1" stop-color="var(--gold-dark)"/>
        </linearGradient>
        <radialGradient id="emblem" cx=".5" cy=".5" r=".5">
          <stop offset="0" stop-color="#f0912c" stop-opacity=".55"/>
          <stop offset="1" stop-color="#f0912c" stop-opacity="0"/>
        </radialGradient>
      </defs>
      <g stroke="var(--ink)" stroke-width="1.2" fill="var(--ink)">
        <line x1="95" y1="114" x2="281" y2="114"/>
        <circle cx="188" cy="114" r="2.5"/>
        <line x1="95" y1="237" x2="281" y2="237"/>
        <circle cx="188" cy="237" r="2.5"/>
        <line x1="430" y1="163" x2="546" y2="163"/>
        <circle cx="488" cy="163" r="2.5"/>
        <line x1="674" y1="29" x2="853" y2="29"/>
        <circle cx="763" cy="29" r="2.5"/>
        <line x1="674" y1="148" x2="853" y2="148"/>
        <circle cx="763" cy="148" r="2.5"/>
      </g>
      <polygon points="488,10 597,73 597,199 488,262 379,199 379,73" fill="none" stroke="url(#gold)" stroke-width="5"/>
      <polygon points="488,21 588,78 588,194 488,251 388,194 388,78" fill="none" stroke="url(#gold)" stroke-width="1.6"/>
      <ellipse cx="488" cy="60" rx="26" ry="22" fill="url(#emblem)" role="img" aria-label="Illustration einer Biene auf Honigwaben"/>
    </svg>

    <div class="sans operator__heading">Abfüllstelle:</div>
    <div class="serif operator__address">Imkerei Henrik Dollmann<br>Lindenkamper W. 17<br>07318 Saalfeld</div>
    <div class="sans operator__phone">Tel.: 03671 5274061</div>
    <div class="sans operator__web">www.wabenhof-laden.example</div>
    <div class="sans shop-name"><span class="shop-name__dot"></span>Wabenhof Laden</div>

    <div class="serif honey__country">DEUTSCHER</div>
    <div class="serif honey__name">HONIG</div>
    <div class="serif honey__weight">500&nbsp;g</div>

    <div class="field field--type" aria-label="Feld für Honigsorte"></div>

    <div class="sans field-label field-label--best">Mindestens haltbar bis:</div>
    <div class="field field--best"></div>
    <div class="sans field-label field-label--lot">Losnummer:</div>
    <div class="field field--lot"></div>
    <div class="sans infant-warning">Nicht geeignet für Säuglinge unter 12 Monaten.</div>
  </div>
</div>
</body>
</html>
```